Hacienda Las Bruneras Website

I need a template design for Hacienda Las Bruneras which is a Residential and Commercial development project to be located in Panama.

The look of the website has to be "country" since it is a Hacienda. It has to take in the feel of being out with nature.

The Logo of the project is contained in the attached files as well as pictures of the Project´s conceptual design and several air pictures of the land where the project will be built.

Industry/Entity Type

Residential

Requirements
Must have
• The website has to be very simple, very visual, a lot of images. The Main Menu has to be:
1. Home
2. About us
3. The project
4. Location
5. Contact us

```html
<!DOCTYPE html>
<html lang="en">
<head>
<meta charset="utf-8">
<title>Hacienda Las Bruneras</title>
<link href="https://fonts.googleapis.com/css2?family=Pathway+Gothic+One&family=Cabin+Condensed:wght@600&display=swap" rel="stylesheet">
<style>
  :root {
    --backdrop-top: #55524a;
    --backdrop-mid: #7a7144;
    --backdrop-bottom: #3f3a24;
    --parchment-light: #f1d9ad;
    --parchment-deep: #d7a464;
    --band-red: #b5342b;
    --band-dark: #7d1d17;
    --nav-text: #fff6e6;
    --brand-text: #9a6a1c;
    --body-bg: #fdf4dc;
    --body-text: #2a1c0e;
    --badge: #8a5a22;
    --photo-one: #7b8468;
    --photo-two: #72805e;
    --photo-three: #596c46;
  }
  * { box-sizing: border-box; margin: 0; padding: 0; }
  html, body { width: 1200px; height: 850px; overflow: hidden; }
  body { position: relative; font-family: "Cabin Condensed", "Arial Narrow", sans-serif; }

  .backdrop {
    position: absolute; inset: 0;
    background: linear-gradient(180deg, var(--backdrop-top) 0%, var(--backdrop-mid) 55%, var(--backdrop-bottom) 100%);
  }

  .site {
    position: absolute; left: 165px; top: 50px; width: 867px; height: 740px;
    background: var(--body-bg);
    box-shadow: 0 0 18px rgba(0,0,0,0.55);
  }

  .masthead {
    position: relative; height: 172px;
    background: radial-gradient(ellipse at 50% 40%, var(--parchment-light) 0%, var(--parchment-deep) 100%);
  }
  .brand-mark {
    position: absolute; left: 397px; top: -42px; width: 72px; height: 66px;
    background: var(--badge); border-radius: 6px;
    box-shadow: 0 2px 4px rgba(0,0,0,0.4);
  }
  .brand-name {
    position: absolute; left: 0; right: 0; top: 36px; text-align: center;
    font-family: "Cabin Condensed", "Arial Narrow", sans-serif; font-weight: 600;
    font-size: 58px; line-height: 72px; color: var(--brand-text); letter-spacing: 1px;
  }
  .main-nav {
    position: absolute; left: 0; right: 0; bottom: 0; height: 45px;
    background: linear-gradient(180deg, var(--band-red) 0%, var(--band-dark) 100%);
  }
  .main-nav a {
    position: absolute; top: 8px; transform: translateX(-50%);
    font-family: "Pathway Gothic One", "Arial Narrow", sans-serif;
    font-size: 21px; line-height: 28px; color: var(--nav-text); text-decoration: none; white-space: nowrap;
  }

  .gallery-shot { position: absolute; left: 32px; width: 288px; }
  .shot-gate { top: 217px; height: 144px; background: var(--photo-one); }
  .shot-avenue { top: 385px; height: 140px; background: var(--photo-two); }
  .shot-roundabout { top: 550px; height: 141px; background: var(--photo-three); }

  .intro-copy {
    position: absolute; left: 335px; top: 232px; width: 512px;
    text-align: center; font-weight: 600; font-size: 13.4px; line-height: 26px;
    color: var(--body-text);
  }
  .intro-copy p + p { margin-top: 26px; }
</style>
</head>
<body>
  <div class="backdrop" role="img" aria-label="Countryside at sunset: cloudy sky over a grassy field with a dirt path"></div>

  <main class="site">
    <header class="masthead">
      <div class="brand-mark"></div>
      <div class="brand-name">Hacienda Las Bruneras</div>
      <nav class="main-nav">
        <a href="#" style="left:155px">Home</a>
        <a href="#" style="left:281px">About Us</a>
        <a href="#" style="left:422px">The Project</a>
        <a href="#" style="left:561px">Location</a>
        <a href="#" style="left:698px">Contact Us</a>
      </nav>
    </header>

    <div class="gallery-shot shot-gate" role="img" aria-label="Rendering of the development's stone entrance gate with pergola"></div>
    <div class="gallery-shot shot-avenue" role="img" aria-label="Rendering of the tree-lined main avenue"></div>
    <div class="gallery-shot shot-roundabout" role="img" aria-label="Aerial rendering of the landscaped roundabout with fountain"></div>

    <section class="intro-copy">
      <p>Lorem ipsum dolor sit amet, consectetur adipiscing elit. Praesent lacinia ut felis vitae pellentesque. Sed ut massa quam. Maecenas tempor ipsum nec odio varius, ac facilisis purus mollis. Nam ipsum nunc, tempus eu erat non, consectetur auctor justo. Praesent eros ante, varius sit amet tellus iaculis, tristique ultricies ante. Duis vulputate placerat sagittis. Integer ac consequat leo, in eleifend nisi. Praesent a vestibulum magna. Aenean id est nibh. Vestibulum pulvinar scelerisque est sed aliquet. Duis dignissim erat dolor, nec tincidunt arcu porta sit amet. Suspendisse accumsan suscipit tortor lobortis convallis. Quisque a mauris nibh.</p>
      <p>Integer vestibulum, elit nec bibendum eleifend, lorem magna pretium ipsum, at tincidunt lectus elit vel neque. Phasellus tincidunt sem lectus, vel placerat libero hendrerit vel. Nulla facilisi. Pellentesque suscipit dolor eget consequat cursus. Cras eu dignissim sem. Donec sit amet euismod ante. Sed mollis vehicula fringilla. Pellentesque habitant morbi tristique senectus et netus et malesuada fames ac turpis egestas. Vestibulum eget dolor eu nulla tristique posuere vitae in felis.</p>
      <p>Nullam pulvinar, lectus at faucibus porta, neque purus facilisis nisl, vitae lacinia urna odio sit amet nulla. Nam semper luctus risus, at pellentesque dolor volutpat eu. Vivamus felis felis, ultrices at massa at, rhoncus convallis ligula.</p>
    </section>
  </main>
</body>
</html>
```